THE ORCHARD BELOW book cover needed

Hello friends! I'm working toward self-publishing my first novel in the next few months, and I'm looking to have a professional-looking, 6 in x 9 in cover to go along with the ebook release. I’m not looking for much, but the key is that it must look professional. I don’t want decorative fonts, but I also don’t want it to just look like Helvetica or Times New Roman.The text for the cover should be:A TIME FOR GREATNESSKARLIS WILDEI have attached a few images to show you where my head is at. I created a book cover myself on paint that looks horribly amateur, but it draws inspiration from a HPM campaign poster(also attached) where the title of the novel comes from. If you can make that same kind of cover, but make it look professional, that would be amazing! If you have other, simple ideas, I am also very, very open.Attached as well are a couple of simple, recent book covers that I like. That is the kind of thing that I am looking for.If this goes well, I may do a paperback release. In that case, I may need to contact you again for an additional fee to create the rest of the wraparound design. In addition, the book is the first in a projected trilogy, so there may be opportunities for you in the future for sequel covers.About the book: THE ORCHARD BELOW is a gripping, standalone thriller with an exciting take on history, relationships, conspiracy theories, and the current, volatile political state of America. In the present day, new information surrounding the 1963 assassination of Harold P. Merrow comes to light and Teodor Vasquelle, a young, best-selling journalist still reconciling his success with his dark past, finds himself more personally connected than he ever could have expected. But the story becomes something even bigger when an assassination attempt on the current demagogic president sends the whole world of journalism into a scramble, and Teodor finds himself confronted by an extremely difficult question: Is democracy real, or has it been an illusion fostered by these secretive ‘Wardens of the Ledger’ since 1776? Travelling across Syria, Canada, and the United States of America, the story becomes more unbelievable—and more personal—as increasingly prominent figures begin to enter Teodor’s orbit, intent on keeping their secrets safe by whatever means necessary.

Colors

Designer to choose colors to be used in the design.

Requirements
Must have
• Text
• Simplicity
• Professional look
Should not have
• Cheap fonts
• Complicated images

```html
<!DOCTYPE html>
<html lang="en">
<head>
<meta charset="utf-8">
<title>The Orchard Below — Wraparound Cover</title>
<link rel="stylesheet" href="https://fonts.googleapis.com/css2?family=Big+Shoulders+Stencil+Display:wght@800&family=Oswald:wght@300;400&family=Jost:wght@500&display=swap">
<style>
  :root {
    --page: #ffffff;
    --flag-navy: #2b3550;
    --flag-red: #b3261c;
    --flag-deep-red: #7a140f;
    --flag-cream: #c9c29a;
    --ink-light: #ffffff;
    --ink-soft: #f3efe4;
  }
  html, body {
    margin: 0;
    width: 1200px;
    height: 1200px;
    overflow: hidden;
    background: var(--page);
  }
  .canvas {
    position: relative;
    width: 1200px;
    height: 1200px;
  }
  .wraparound {
    position: absolute;
    left: 33px;
    top: 207px;
    width: 1135px;
    height: 785px;
    overflow: hidden;
  }
  .flag-art {
    position: absolute;
    inset: 0;
    width: 100%;
    height: 100%;
  }
  .back-copy {
    position: absolute;
    left: 51px;
    width: 425px;
    margin: 0;
    font-family: "Jost", sans-serif;
    font-weight: 500;
    font-variant: small-caps;
    font-size: 19px;
    line-height: 21.8px;
    letter-spacing: 1.8px;
    text-align: center;
    color: var(--ink-light);
  }
  .back-copy--main { top: 117px; }
  .back-copy--second { top: 480px; }
  .spine-text {
    position: absolute;
    writing-mode: vertical-rl;
    font-family: "Oswald", sans-serif;
    font-weight: 400;
    color: var(--ink-light);
    font-size: 34px;
    line-height: 1;
    letter-spacing: 0.5px;
    left: 550px;
  }
  .spine-title { top: 63px; }
  .spine-author { top: 533px; }
  .front-title {
    position: absolute;
    left: 600px;
    top: 0;
    width: 546px;
    height: 600px;
    margin: 0;
    font-family: "Big Shoulders Stencil Display", sans-serif;
    font-weight: 800;
    color: var(--ink-light);
    font-size: 125px;
    line-height: 148px;
    letter-spacing: 1px;
  }
  .front-title span {
    position: absolute;
    left: 0;
    width: 100%;
    text-align: center;
  }
  .front-title .line-1 { top: 90px; }
  .front-title .line-2 { top: 238px; }
  .front-title .line-3 { top: 386px; }
  .front-tag {
    position: absolute;
    left: 990px;
    top: 188px;
    font-family: "Oswald", sans-serif;
    font-weight: 300;
    font-style: italic;
    font-size: 33px;
    line-height: 1;
    color: var(--ink-soft);
    white-space: nowrap;
  }
  .front-author {
    position: absolute;
    left: 600px;
    width: 546px;
    top: 700px;
    text-align: center;
    font-family: "Oswald", sans-serif;
    font-weight: 400;
    font-size: 60px;
    line-height: 1;
    letter-spacing: 1px;
    color: var(--ink-light);
  }
</style>
</head>
<body>
<main class="canvas">
  <section class="wraparound">
    <svg class="flag-art" viewBox="0 0 1135 785" preserveAspectRatio="none" role="img" aria-label="Weathered, grunge-textured waving American flag with stars on navy and red and cream stripes">
      <defs>
        <linearGradient id="flagTone" x1="0" y1="0" x2="1" y2="1">
          <stop offset="0" stop-color="var(--flag-navy)"/>
          <stop offset="0.35" stop-color="#6a5a48"/>
          <stop offset="0.55" stop-color="var(--flag-red)"/>
          <stop offset="1" stop-color="var(--flag-deep-red)"/>
        </linearGradient>
      </defs>
      <rect width="1135" height="785" fill="url(#flagTone)"/>
    </svg>

    <p class="back-copy back-copy--main">Lorem ipsum dolor sit amet, consectetur adipiscing elit, sed do eiusmod tempor incididunt ut labore et dolore magna aliqua. Ut enim ad minim veniam, quis nostrud exercitation ullamco laboris nisi ut aliquip ex ea commodo consequat. Duis aute irure dolor in reprehenderit in voluptate velit esse cillum dolore eu fugiat nulla pariatur. Excepteur sint occaecat cupidatat non proident, sunt in culpa qui officia deserunt mollit anim id est laborum.</p>
    <p class="back-copy back-copy--second">Lorem ipsum dolor sit amet, consectetur adipiscing elit, sed do eiusmod tempor incididunt ut labore et dolore magna aliqua. Ut enim ad minim veniam, quis nostrud exercitation ullamco laboris nisi ut aliquip ex ea commodo consequat.</p>

    <div class="spine-text spine-title">THE ORCHARD BELOW</div>
    <div class="spine-text spine-author">BRENNO SALTVIK</div>

    <h1 class="front-title">
      <span class="line-1">THE</span>
      <span class="line-2">ORCHARD</span>
      <span class="line-3">BELOW</span>
    </h1>
    <div class="front-tag">A NOVEL</div>
    <div class="front-author">BRENNO SALTVIK</div>
  </section>
</main>
</body>
</html>
```